Stretch Depot Community Wordpress Site

Branding package: http://www.stretchdepot.example/drop/Stretch_Depot_Branding_v02.pdf
**please reference above branding package when creating theme.
The goal is to have the site come off industrious and functional. A warehouse feel without being too cold.
We are looking for a theme/skin for our wordpress site. The blog has already been setup and all necessary plugins have been installed.
Stretch Depot is the local yoga enthusiasts online portal for information regarding yoga in the community. It is a place to share experiences, events, knowledge, and encouragement, ultimately serving to build community and connect people in their love for the practice of yoga.
Work with the concept of a warehouse, it is a warehouse of ideas.
Some keywords that describe the site:
Energetic, friendly, welcoming, industrious, fun, confident, charming, grounded, functional.
Color Palette: http://www.stretchdepot.example/drop/color-palette.png
Logo: http://www.stretchdepot.example/drop/logo.png
Reason: Have not found something that is a good fit.
Target Market(s)
Predominantly women, mid 20s to mid 40s however appeals to anyone one looking for yoga in the area and while its predominantly females the site should have a masculine look.
Industry/Entity Type
Events
Requirements
Must have
- Must use the color palette
Must use provided logo
Should not have
- plain white background.

```html
<!DOCTYPE html>
<html lang="en">
<head>
<meta charset="utf-8">
<title>Stretch Depot — Community</title>
<link href="https://fonts.googleapis.com/css2?family=Oswald:wght@400;500&family=Arimo:wght@400;700&family=Ubuntu:wght@400&display=swap" rel="stylesheet">
<style>
:root{
  --purple:#5e2360;
  --purple-btn:#6b2a6e;
  --slate:#4a6274;
  --ink:#1c1c1c;
  --panel:#1f1f1f;
  --sky:#7db6e3;
  --sky-light:#a9d0ef;
  --backdrop:#e3e3e3;
  --paper:#f8f8f8;
  --footer:#ececec;
  --rule:#cfcfcf;
  --text:#2a2a2a;
  --star:#5aa3e0;
}
*{box-sizing:border-box;margin:0;padding:0}
html,body{width:758px;height:1200px;overflow:hidden}
body{background:var(--backdrop);font-family:"Arimo",Arial,sans-serif;color:var(--text);position:relative}
.abs{position:absolute}

.page{position:absolute;left:76px;top:24px;width:606px;height:1176px;background:var(--paper);border-radius:8px 8px 0 0;box-shadow:0 0 6px rgba(0,0,0,.15)}
.inner{position:absolute;left:76px;top:0;width:606px;height:1200px}

/* header */
.brand{left:24px;top:44px;font-family:"Oswald",sans-serif;font-weight:500;font-size:22px;line-height:30px;color:var(--purple)}
.social{display:flex;gap:6px}
.social span{width:17px;height:17px;border-radius:3px;background:#8a9aa6}
.header-social{left:377px;top:39px}
.search{left:452px;top:38px;width:140px;height:18px;border:1px solid #c8c8c8;border-radius:3px;background:#fff;font-size:8px;color:#aaa;padding:4px 8px}
.search svg{position:absolute;right:0;top:0;width:20px;height:16px;border-left:1px solid #ccc}
.nav{left:273px;top:72px;width:329px;height:32px;border:1px solid #d0d0d0;background:#fafafa;display:flex}
.nav a{flex:auto;text-align:center;font-family:"Oswald",sans-serif;font-weight:500;font-size:14px;color:#222;text-decoration:none;line-height:30px;border-right:1px solid #d4d4d4}
.nav a:last-child{border-right:0}

/* slider */
.slider{left:5px;top:108px;width:597px;height:206px;border:1px solid #9aa;box-shadow:0 6px 8px rgba(0,0,0,.25)}
.slide-photo{left:0;top:0;width:595px;height:179px;background:linear-gradient(90deg,#3e5a2a,#6d8a4a 30%,#d8dcd6 50%,#789a58 70%,#3c5528)}
.featured{left:409px;top:129px;background:#2d8fd8;color:#fff;font-size:7px;padding:2px 7px}
.caption{left:409px;top:140px;width:186px;height:29px;background:rgba(0,0,0,.72);color:#fff;font-family:"Oswald",sans-serif;font-weight:500;font-size:16px;letter-spacing:1.5px;padding:3px 8px}
.slider-bar{left:0;top:179px;width:595px;height:25px;background:var(--slate);border-top:1px solid #6c8595}
.slider-bar .prev,.slider-bar .next{position:absolute;top:0;height:24px;line-height:23px;color:#fff;font-family:"Oswald",sans-serif;font-size:13px;padding:0 7px;border-color:#2e3e4a}
.prev{left:0;border-right:1px solid}
.next{right:0;border-left:1px solid}
.dots{left:282px;top:8px;display:flex;gap:3px}
.dots i{width:9px;height:9px;border-radius:50%;background:#1b2328}
.dots i:first-child{border:1px solid #3ba0e8}

/* feature thumbs */
.band{left:0;top:363px;width:606px;height:104px;background:var(--slate)}
.thumb{top:337px;width:135px;height:134px;box-shadow:0 3px 5px rgba(0,0,0,.35)}
.thumb .shade{position:absolute;left:0;bottom:0;width:100%;height:58px;background:rgba(50,50,50,.6);color:#fff;padding:22px 10px 0}
.thumb small{font-size:7px;display:block}
.thumb b{font-weight:400;font-size:10px;line-height:10px;display:block}

/* latest news */
.news-tab{left:0;top:489px;width:166px;height:39px;background:var(--ink);clip-path:polygon(0 0,100% 0,88% 100%,0 100%)}
.news-tab h2{color:#fff;font-family:"Oswald",sans-serif;font-weight:500;font-size:19px;padding:7px 22px}
.post{left:21px;width:400px}
.post-img{position:absolute;left:0;top:0;width:90px;height:91px;box-shadow:0 3px 4px rgba(0,0,0,.3)}
.post-body{position:absolute;left:101px;top:6px;width:296px}
.post-date{font-family:"Oswald",sans-serif;font-size:8px;color:#222}
.post-title{font-family:"Oswald",sans-serif;font-weight:400;font-size:12px;color:var(--purple);margin-top:6px}
.post-text{font-size:7.3px;line-height:10px;margin-top:5px;color:#222}
.post-actions{display:flex;align-items:center;gap:8px;margin-top:9px}
.btn{display:inline-block;background:var(--purple-btn);color:#fff;font-family:"Oswald",sans-serif;font-size:8px;text-transform:uppercase;padding:3px 8px;border-radius:2px;box-shadow:0 0 0 1px #c9a9cc}
.comments{font-family:"Oswald",sans-serif;font-size:9px;color:var(--slate)}
.rule{left:19px;width:399px;height:1px;background:var(--rule)}
.all-articles{left:15px;top:918px;font-family:"Oswald",sans-serif;font-size:10px;color:#222}

/* popular */
.popular{left:437px;top:489px;width:169px;height:449px;background:var(--panel)}
.popular h3{position:absolute;left:17px;top:12px;color:var(--star);font-family:"Oswald",sans-serif;font-weight:500;font-size:14px;display:flex;gap:10px;align-items:center}
.pop-item{left:18px;width:140px}
.pop-img{position:absolute;left:0;top:0;width:60px;height:60px;border:1px solid #444}
.pop-text{position:absolute;left:67px;top:16px;color:#fff;font-family:"Oswald",sans-serif;width:68px}
.pop-text b{font-weight:400;font-size:9px;display:block}
.pop-text small{font-size:6px;line-height:7px;display:block;color:#ddd}
.pop-rule{left:16px;width:138px;height:1px;background:#444}
.all-news{left:17px;top:429px;color:#fff;font-family:"Oswald",sans-serif;font-size:9px}

/* promo band */
.promo{left:0;top:938px;width:606px;height:102px;background:linear-gradient(180deg,var(--sky-light),var(--sky) 40%)}
.promo-img{top:24px;width:92px;height:56px;border:2px solid #555;box-shadow:0 2px 3px rgba(0,0,0,.3)}
.promo-copy{left:428px;top:22px;width:166px;text-align:center;color:#fff;font-family:"Oswald",sans-serif}
.promo-copy p{font-size:13px;line-height:15px;white-space:nowrap}
.promo-copy .sub{display:block;font-size:10px;margin-top:1px}
.promo-copy .btn{background:#3a3a3a;margin-top:4px;box-shadow:0 0 0 1px #888}

/* footer */
.footer{left:0;top:1040px;width:606px;height:160px;background:var(--footer)}
.footer h4{position:absolute;top:20px;font-family:"Ubuntu",sans-serif;font-weight:400;font-size:12px;color:var(--purple)}
.footer ul{position:absolute;top:41px;list-style:none;font-size:7.3px;line-height:15.2px;color:#333}
.footer .address{position:absolute;left:366px;top:41px;font-size:7.3px;line-height:15.2px;color:#333}
.footer-social{left:366px;top:86px}
.copyright{right:18px;top:141px;font-size:7px;color:#888}
</style>
</head>
<body>
<div class="page"></div>
<div class="inner">

<!-- header -->
<div class="abs brand">Stretch Depot</div>
<div class="abs social header-social"><span></span><span></span><span></span></div>
<div class="abs search">search...
  <svg viewBox="0 0 20 16"><circle cx="9" cy="7" r="3" fill="none" stroke="#555" stroke-width="1.3"/><line x1="11.2" y1="9.2" x2="13.5" y2="11.5" stroke="#555" stroke-width="1.3"/></svg>
</div>
<nav class="abs nav"><a>HOME</a><a>GALLERY</a><a>BLOG</a><a>ABOUT</a><a>CONTACT</a></nav>

<!-- slider -->
<div class="abs slider">
  <div class="abs slide-photo" role="img" aria-label="Woman meditating in a white blouse in a green garden"></div>
  <div class="abs featured">FEATURED</div>
  <div class="abs caption">YOGA DIVINE</div>
  <div class="abs slider-bar">
    <span class="prev">&lsaquo;PREVIOUS</span>
    <div class="abs dots"><i></i><i></i><i></i></div>
    <span class="next">NEXT&rsaquo;</span>
  </div>
</div>

<!-- feature thumbs -->
<div class="abs band"></div>
<div class="abs thumb" style="left:11px;background:linear-gradient(180deg,#e8e4de,#c8b9a4 60%,#9c8a76)" role="img" aria-label="Woman stretching on a beach"><div class="shade"><small>11 JAN</small><b>LOREM IPSUM SET<br>AMIT DOLOR</b></div></div>
<div class="abs thumb" style="left:161px;background:linear-gradient(180deg,#c9d2a8,#9a9a80 50%,#4a4a40)" role="img" aria-label="Woman in prayer pose on a porch"><div class="shade"><small>11 JAN</small><b>LOREM IPSUM SET<br>AMIT DOLOR</b></div></div>
<div class="abs thumb" style="left:310px;background:linear-gradient(180deg,#a66a52,#b8aea2 40%,#3a5f9a 70%,#6a6660)" role="img" aria-label="Woman in warrior pose by a stone wall"><div class="shade"><small>11 JAN</small><b>LOREM IPSUM SET<br>AMIT DOLOR</b></div></div>
<div class="abs thumb" style="left:460px;background:linear-gradient(180deg,#f4f2ef,#d9b89a 50%,#b08a6c)" role="img" aria-label="Woman in a side stretch on a white background"><div class="shade"><small>11 JAN</small><b>LOREM IPSUM SET<br>AMIT DOLOR</b></div></div>

<!-- latest news -->
<div class="abs news-tab"><h2>LATEST NEWS</h2></div>

<article class="abs post" style="top:545px">
  <div class="post-img" style="background:linear-gradient(160deg,#c9d3d6,#b46d62 50%,#5c6a7a)" role="img" aria-label="Group yoga class in a gym"></div>
  <div class="post-body">
    <div class="post-date">4 FEB 2012</div>
    <h3 class="post-title">LOREM IPSUM DOLOR SIT AMET</h3>
    <p class="post-text">Lorem ipsum dolor sit amet, consectetur adipiscing elit. Mauris luctus varius feugiat. In ultricies lacinia nulla sit amet molestie. Suspendisse ut nisl ac lorem pulvinar.</p>
    <div class="post-actions"><span class="btn">Read more</span><span class="comments">56 COMMENTS</span></div>
  </div>
</article>
<div class="abs rule" style="top:652px"></div>

<article class="abs post" style="top:669px">
  <div class="post-img" style="background:linear-gradient(180deg,#6b6a60,#d7c07a 55%,#2a2a22)" role="img" aria-label="Silhouette in a yoga pose at sunset"></div>
  <div class="post-body">
    <div class="post-date">5 FEB 2012</div>
    <h3 class="post-title">LOREM IPSUM DOLOR SIT AMET</h3>
    <p class="post-text">Lorem ipsum dolor sit amet, consectetur adipiscing elit. Mauris luctus varius feugiat. In ultricies lacinia nulla sit amet molestie. Suspendisse ut nisl ac lorem pulvinar.</p>
    <div class="post-actions"><span class="btn">Read more</span><span class="comments">63 COMMENTS</span></div>
  </div>
</article>
<div class="abs rule" style="top:778px"></div>

<article class="abs post" style="top:796px">
  <div class="post-img" style="background:linear-gradient(135deg,#3a3430,#c4a48c 50%,#4c4440)" role="img" aria-label="Instructor assisting a student in class"></div>
  <div class="post-body">
    <div class="post-date">6 FEB 2012</div>
    <h3 class="post-title">LOREM IPSUM DOLOR SIT AMET</h3>
    <p class="post-text">Lorem ipsum dolor sit amet, consectetur adipiscing elit. Mauris luctus varius feugiat. In ultricies lacinia nulla sit amet molestie. Suspendisse ut nisl ac lorem pulvinar.</p>
    <div class="post-actions"><span class="btn">Read more</span><span class="comments">80 COMMENTS</span></div>
  </div>
</article>
<div class="abs rule" style="top:906px"></div>
<div class="abs all-articles"><svg width="6" height="7" viewBox="0 0 6 7"><path d="M5 0 L0 3.5 L5 7Z" fill="#222"/></svg> ALL ARTICLES</div>

<!-- popular news -->
<aside class="abs popular">
  <h3><svg width="13" height="13" viewBox="0 0 24 24"><path d="M12 2l3 7 7 .6-5.4 4.7 1.7 7.3L12 17.8 5.7 21.6l1.7-7.3L2 9.6 9 9z" fill="#5aa3e0"/></svg>POPULAR NEWS<svg width="13" height="13" viewBox="0 0 24 24"><path d="M12 2l3 7 7 .6-5.4 4.7 1.7 7.3L12 17.8 5.7 21.6l1.7-7.3L2 9.6 9 9z" fill="#5aa3e0"/></svg></h3>

  <div class="abs pop-item" style="top:44px"><div class="pop-img" style="background:linear-gradient(180deg,#c8b8a6,#b05a4a 60%,#3a3a44)" role="img" aria-label="Women in a yoga class"></div><div class="pop-text"><b>LOREM IPSUM</b><small>LOREM IPSUM DOLOR SIT AMET, CONSECTETUR</small></div></div>
  <div class="abs pop-rule" style="top:125px"></div>
  <div class="abs pop-item" style="top:145px"><div class="pop-img" style="background:linear-gradient(180deg,#b4c2cc,#d6cfc6 50%,#4a4e5a)" role="img" aria-label="Class seated in meditation"></div><div class="pop-text"><b>LOREM IPSUM</b><small>LOREM IPSUM DOLOR SIT AMET, CONSECTETUR</small></div></div>
  <div class="abs pop-rule" style="top:226px"></div>
  <div class="abs pop-item" style="top:249px"><div class="pop-img" style="background:linear-gradient(180deg,#f2f2f2,#d0a08a 55%,#e6e6e6)" role="img" aria-label="Woman in a plank pose"></div><div class="pop-text"><b>LOREM IPSUM</b><small>LOREM IPSUM DOLOR SIT AMET, CONSECTETUR</small></div></div>
  <div class="abs pop-rule" style="top:330px"></div>
  <div class="abs pop-item" style="top:353px"><div class="pop-img" style="background:linear-gradient(180deg,#9aa6b0,#b88a70 50%,#6a5c54)" role="img" aria-label="Outdoor group exercise class"></div><div class="pop-text"><b>LOREM IPSUM</b><small>LOREM IPSUM DOLOR SIT AMET, CONSECTETUR</small></div></div>
  <div class="abs all-news">ALL NEWS</div>
</aside>

<!-- promo band -->
<section class="abs promo">
  <div class="abs promo-img" style="left:18px;background:linear-gradient(180deg,#c9d2a8,#9a9a80 50%,#4a4a40)" role="img" aria-label="Woman in prayer pose"></div>
  <div class="abs promo-img" style="left:118px;background:linear-gradient(180deg,#f4f2ef,#d8a888 55%,#f0eeea)" role="img" aria-label="Woman stretching arms overhead"></div>
  <div class="abs promo-img" style="left:218px;background:linear-gradient(180deg,#f4f2ef,#d6b49a 55%,#efece8)" role="img" aria-label="Woman in a side bend"></div>
  <div class="abs promo-img" style="left:319px;background:linear-gradient(180deg,#a66a52,#b8aea2 45%,#3a5f9a)" role="img" aria-label="Woman in warrior pose by a wall"></div>
  <div class="abs promo-copy">
    <p>LOREM IPSUM DOLOR SIT AMET,<br>CONSECTETUR ADIPISCING ELIT.</p>
    <span class="sub">MAURIS LUCTUS VARIUS FEUGIAT</span>
    <span class="btn">Read more</span>
  </div>
</section>

<!-- footer -->
<footer class="abs footer">
  <h4 style="left:23px">Categories</h4>
  <h4 style="left:174px">Links</h4>
  <h4 style="left:276px">Archives</h4>
  <h4 style="left:364px">Get in touch</h4>
  <ul style="left:23px"><li>Proin eget</li><li>Orci a nulla</li><li>Consequat</li><li>Hendrerit</li><li>Nunc non</li><li>Dictum quam</li></ul>
  <ul style="left:88px"><li>Lorem</li><li>Ipsum</li><li>Dolor sit amet</li><li>Consectetur</li><li>Adipiscing elit</li><li>Sed consequat</li></ul>
  <ul style="left:175px"><li>Link 1</li><li>Another cool link</li><li>More links here</li><li>Just another one</li><li>Fifth link here</li><li>Last one in here</li></ul>
  <ul style="left:277px"><li>May 2011</li><li>April 2011</li><li>March 2011</li><li>February 2011</li><li>January 2011</li></ul>
  <div class="address">Some road or street in Some Place of one Country in the Globe.<br>Street of success 20952 - Location of the office<br>Phone: 0100-55-0100-2000 &nbsp;&nbsp; Fax: 0100-55-0100-2001</div>
  <div class="abs social footer-social"><span></span><span></span><span></span></div>
  <div class="abs copyright">© Copyright 2012 Stretchdepot.example. All Rights Reserved</div>
</footer>

</div>
</body>
</html>
```